Fernvale Business Card Design

We are looking for a fresh business card design for our new logo. We would like a business card that is unique but friendly. We are in the window coverings business offering blinds, shutters and shades for homes.

Target Market(s)

Targeting the end-consumer

Industry/Entity Type

Business

Requirements
Must have
• Must have a dedicates space for a photo of our sales person. Must contain our new logo (attached).

```html
<!DOCTYPE html>
<html lang="en">
<head>
<meta charset="utf-8">
<title>Fernvale Business Card</title>
<link rel="stylesheet" href="https://fonts.googleapis.com/css2?family=Tenor+Sans&family=Open+Sans:wght@400;600&display=swap">
<style>
  :root {
    --backdrop: #ececed;
    --card-white: #fbfbfb;
    --leaf-green: #8cc540;
    --slate: #646469;
    --ink: #1e1e20;
    --photo-tone: #2a2a2e;
  }
  html, body {
    margin: 0;
    width: 1200px;
    height: 1200px;
    overflow: hidden;
    background: var(--backdrop);
  }
  .canvas { position: relative; width: 1200px; height: 1200px; }

  .card { position: absolute; left: 298px; width: 605px; height: 346px; }
  .card-front { top: 222px; background: var(--card-white); border-radius: 6px; }
  .card-back { top: 633px; background: var(--leaf-green); border-radius: 32px; }

  .brand-square {
    position: absolute; left: 32px; top: 30px;
    width: 120px; height: 120px;
    box-sizing: border-box;
    border: 5px solid var(--slate);
    border-radius: 4px;
  }
  .brand-name {
    position: absolute; left: 180px; top: 40px;
    margin: 0;
    font-family: "Tenor Sans", sans-serif;
    font-weight: 400;
    font-size: 92px;
    line-height: 1;
    color: var(--slate);
  }

  .contact-list {
    position: absolute; left: 31px; top: 225px;
    margin: 0; padding: 0; list-style: none;
    font-family: "Open Sans", sans-serif;
    font-size: 11.5px;
    letter-spacing: 0.6px;
    line-height: 19.3px;
    color: var(--ink);
  }
  .contact-label { color: var(--leaf-green); }

  .rep { position: absolute; left: 376px; top: 152px; width: 160px; text-align: center; }
  .rep-photo {
    display: block; margin: 0 auto;
    width: 96px; height: 96px; border-radius: 50%;
    background: radial-gradient(circle at 50% 45%, #6b5a52 0 28%, var(--photo-tone) 60%);
    border: 1.5px solid var(--leaf-green);
    box-sizing: border-box;
  }
  .rep-name {
    margin: 6px 0 0;
    font-family: "Open Sans", sans-serif;
    font-weight: 600;
    font-variant: small-caps;
    font-size: 24px;
    line-height: 1;
    color: var(--ink);
  }
  .rep-title {
    margin: 6px 0 0;
    font-family: "Open Sans", sans-serif;
    font-weight: 600;
    font-size: 12.5px;
    letter-spacing: 2.6px;
    color: var(--ink);
  }

  .back-square {
    position: absolute; left: 270px; top: 115px;
    width: 64px; height: 64px;
    box-sizing: border-box;
    border: 3px solid #ffffff;
    border-radius: 3px;
  }
  .back-name {
    position: absolute; left: 0; right: 0; top: 188px;
    margin: 0; text-align: center;
    font-family: "Tenor Sans", sans-serif;
    font-size: 50px; line-height: 1;
    color: #ffffff;
  }
</style>
</head>
<body>
<main class="canvas">
  <section class="card card-front" aria-label="Card front">
    <span class="brand-square" aria-hidden="true"></span>
    <h1 class="brand-name">Fernvale</h1>

    <ul class="contact-list">
      <li><span class="contact-label">phone:</span> 111.111.1111</li>
      <li><span class="contact-label">email:</span> saleman@fernvale.com</li>
      <li><span class="contact-label">web:</span>&nbsp;&nbsp; www.fernvale.com</li>
      <li><span class="contact-label">address:</span> your address goes here.</li>
    </ul>

    <div class="rep">
      <span class="rep-photo" role="img" aria-label="Portrait photo of the sales representative"></span>
      <p class="rep-name">Daniel Hart</p>
      <p class="rep-title">SALE OFFICER</p>
    </div>
  </section>

  <section class="card card-back" aria-label="Card back">
    <span class="back-square" aria-hidden="true"></span>
    <p class="back-name">Fernvale</p>
  </section>
</main>
</body>
</html>
```